Print & digital package needed for technology firm

We need a package of coordinating marketing materials for our technology business. We offer technology solutions to midsized organizations, including data center, outsourced IT, and technology consulting. Find more information on our website, www.pexlora.com. Design is the main concern, we can modify the text ongoing to best reflect our company’s offerings. The design should communicate technology expertise and strategic thinking. Our website is currently being updated with a “flat design” theme and we’d like design of these items to be flat, fresh, modern, and professional, without being boring.
Please use attached logo - can send in .ai/.eps/.psd/etc. Fonts in logo are Futura, Futura Book, and Lato. Please use Pexlora blue, #0372bb.
Please find attached one of our product flyers for one of the computers we lease. Fonts used are Roboto Slab (partial to this font) & Lato. Also attached copy of our business card design.
Taglines we have used include “Does IT hear what troubles you?” and “IT made simple” although we are open to new ideas.
Would like final products to be available in editable files - .psd/.tif/.ai/etc.

- 1 PowerPoint template
- 1 leaderboard ad (digital, 72dpi)
- 1 medium rectangle ad 300x250 (digital, 72dpi)
- 1 full page ad 8x11 (print, 300dpi)
- 1 half-page ad horizontal (print, 300dpi)
- 1 letterhead template
- 1 proposal front-page

There is potential for further graphic/print design opportunities for our business as well.

All, thank you for your assistance in understanding the budget process with this type of design contest - we have updated the project's budget to reflect the items we are requesting.

Please email mvarga at pexlora.com with inquiries or comments. Thank you.

Designers,

Due to an oversight, our project was listed as "refundable" - this has been corrected and changed to committed payment.
To enter into this contest, please pick 2-3 items from the list of desired materials (ads, powerpoint, letterhead, etc.) It is not necessary to submit all items which will be part of the final package to be considered for the contest.

Thank you. Please contact mvarga@pexlora.com for questions.
Best,
Mimi

CEOs, CFOs, CIOs, COOs - college+ educated, 30-60, professional.

```html
<!DOCTYPE html>
<html lang="en">
<head>
<meta charset="utf-8">
<title>Pexlora Presentation Template</title>
<link href="https://fonts.googleapis.com/css2?family=Lato:wght@300;400;700&display=swap" rel="stylesheet">
<style>
  :root{
    --brand-blue:#0372bb;
    --bright-blue:#1a8ad6;
    --sky:#4fb0e6;
    --navy:#2d3440;
    --stage:#5a6069;
    --paper:#f8f8f8;
    --rule:#e4e6e9;
    --ink:#3a3f47;
    --muted:#6d737c;
    --green:#9ccf3a;
    --pink:#e8506e;
    --purple:#a83cb7;
  }
  *{box-sizing:border-box;margin:0;padding:0}
  html,body{width:1064px;height:1200px;overflow:hidden}
  body{background:var(--stage);font-family:"Lato",sans-serif;color:var(--ink);position:relative}
  .slide{position:absolute;width:516px;height:386px;background:var(--paper);overflow:hidden}
  .slide--title{left:12px;top:9px}
  .slide--cover{left:536px;top:9px}
  .slide--portrait{left:12px;top:407px}
  .slide--graphs{left:536px;top:407px}
  .slide--tables{left:12px;top:804px}
  .slide--closing{left:536px;top:804px}

  .brand{font-family:"Lato",sans-serif;font-weight:700;color:var(--brand-blue);letter-spacing:-.2px}
  .corner-fold{position:absolute;right:0;bottom:0;width:22px;height:22px;background:var(--brand-blue);clip-path:polygon(100% 0,100% 100%,0 100%)}
  .network-bg{position:absolute;left:0;top:0;width:300px;height:386px;background:radial-gradient(ellipse at 30% 45%,#eceef0 0%,rgba(248,248,248,0) 70%)}

  /* title slide */
  .question{position:absolute;left:95px;top:193px;font-size:23px;font-weight:300;color:var(--ink);white-space:nowrap}
  .question strong{font-weight:700;color:var(--brand-blue)}
  .slide--title .brand{position:absolute;right:116px;top:224px;font-size:19px}

  /* cover slide */
  .cover-photo{position:absolute;inset:0;background:linear-gradient(135deg,#dfeaf3 0%,#eef4f9 35%,#c9def0 70%,#e4eef6 100%)}
  .cover-lockup{position:absolute;left:10px;top:300px;display:flex;align-items:baseline;gap:8px;white-space:nowrap}
  .cover-lockup .brand{font-size:24px}
  .cover-lockup .tag{font-size:12px;font-style:italic;color:var(--brand-blue);border-left:1px solid var(--brand-blue);padding-left:7px}
  .presenter-bar{position:absolute;left:0;top:331px;width:264px;height:55px;background:var(--navy);padding:14px 10px 0}
  .presenter-bar .name{font-size:12px;font-weight:700;color:#fff;white-space:nowrap}
  .presenter-bar .aud{font-size:8.5px;color:var(--bright-blue)}
  .presenter-bar::after{content:"";position:absolute;right:0;bottom:0;width:20px;height:20px;background:var(--brand-blue);clip-path:polygon(100% 0,100% 100%,0 100%)}
  .cover-title{position:absolute;left:272px;top:334px;font-size:28px;font-weight:300;color:var(--brand-blue);white-space:nowrap}
  .cover-date{position:absolute;left:273px;top:366px;font-size:12px;color:var(--brand-blue)}

  /* dark header */
  .header-dark{position:absolute;left:0;top:0;width:516px;height:37px;background:var(--navy);display:flex;align-items:center;padding-left:10px;gap:9px;white-space:nowrap}
  .header-dark h1{font-size:23px;font-weight:300;color:#fff}
  .header-dark .sub{font-size:12px;color:var(--brand-blue);border-left:1px solid var(--brand-blue);padding-left:7px}
  .header-dark::after{content:"";position:absolute;right:0;bottom:0;width:20px;height:20px;background:var(--brand-blue);clip-path:polygon(100% 0,100% 100%,0 100%)}
  /* light header */
  .header-light{position:absolute;left:0;top:0;width:516px;height:40px;border-bottom:1px solid var(--rule);display:flex;align-items:center;padding-left:10px;gap:8px;white-space:nowrap}
  .header-light h1{font-size:25px;font-weight:300;color:var(--brand-blue)}
  .header-light .sub{font-size:12px;color:var(--muted);border-left:1px solid var(--muted);padding-left:7px}
  .header-light .sub b{color:var(--navy)}

  /* portrait slide */
  .drop-hint{position:absolute;left:32px;top:104px;font-size:13px;color:var(--brand-blue);line-height:1.3}
  .drop-hint .arrow{display:inline-block;width:14px;height:14px;border:1px solid var(--brand-blue);border-radius:50%;font-size:9px;text-align:center;line-height:12px;margin-left:4px;vertical-align:1px}
  .body-copy{position:absolute;left:32px;top:148px;width:210px;font-size:9px;line-height:1.42;text-align:justify;color:var(--ink)}
  .tick-list{position:absolute;left:50px;top:222px;list-style:none;font-size:9px;line-height:16px}
  .tick-list li::before{content:"✓";color:var(--brand-blue);margin-left:-14px;margin-right:7px}
  .image-slot{position:absolute;left:267px;top:64px;width:218px;height:275px;background:#eeeeee;border:1px solid #dcdcdc;display:flex;align-items:center;justify-content:center}
  .footer-light{position:absolute;left:0;bottom:0;width:516px;height:30px;border-top:1px solid var(--rule);display:flex;align-items:center;padding:0 10px;gap:8px;white-space:nowrap}
  .footer-light .brand,.footer-dark .brand{font-size:17px}
  .footer-meta{font-size:8.5px;color:var(--navy)}
  .footer-meta span{color:var(--brand-blue)}
  .footer-light .page{margin-left:auto;font-size:9px;font-weight:700;color:var(--brand-blue);margin-right:4px}
  .footer-dark{position:absolute;left:0;bottom:0;width:516px;height:30px;background:var(--navy);display:flex;align-items:center;padding:0 10px;gap:8px;white-space:nowrap}
  .footer-dark .footer-meta{color:#fff}
  .page-tab{position:absolute;right:0;bottom:0;width:30px;height:30px;background:var(--brand-blue);clip-path:polygon(30% 0,100% 0,100% 100%,0 100%);font-size:8px;font-weight:700;color:#fff;text-align:right;padding:4px 10px 0 0}

  /* graphs slide */
  .graph-title{position:absolute;font-size:14px;font-weight:400;color:var(--ink);white-space:nowrap}
  .graph-title b{font-weight:700}
  .graph-notes{position:absolute;width:200px;list-style:none;font-size:6.5px;line-height:1.35;color:var(--muted)}
  .graph-notes li{position:relative;padding-left:12px;margin-bottom:9px}
  .graph-notes li::before{content:"›";position:absolute;left:0;color:var(--brand-blue);font-size:9px;line-height:8px}
  .graph-notes b{color:var(--navy)}

  /* tables */
  .table-title{position:absolute;top:59px;font-size:15px;color:var(--navy);display:flex;align-items:center;gap:5px}
  .table-title svg{display:block}
  .task-table{position:absolute;top:85px;width:230px;border-collapse:collapse;font-size:5.2px;table-layout:fixed}
  .task-table th{height:22px;font-size:8px;font-weight:700;color:#fff;text-align:center}
  .task-table td{height:22.5px;padding:0 3px;vertical-align:middle;line-height:1.15}
  .task-table tbody td:first-child{text-align:center;font-size:8.5px;color:var(--brand-blue)}
  .task-table tbody td:last-child{text-align:center}
  .task-table tfoot td{height:22px;font-size:8px;text-align:center}
  .task-table--light{left:20px}
  .task-table--light th{background:var(--navy)}
  .task-table--light tbody td{color:var(--muted);border-bottom:1px solid var(--rule)}
  .task-table--light tfoot td{background:var(--brand-blue);color:#fff}
  .task-table--dark{left:268px}
  .task-table--dark th{background:var(--brand-blue)}
  .task-table--dark tbody td{background:var(--navy);color:#b9c1cc;border-bottom:1px solid #3a4350}
  .task-table--dark tfoot td{background:var(--navy);color:var(--bright-blue)}

  /* closing */
  .closing-brand{position:absolute;left:0;width:516px;top:168px;text-align:center}
  .closing-brand .brand{font-size:37px}
  .closing-tag{position:absolute;right:132px;top:216px;font-size:12px;font-style:italic;color:var(--brand-blue)}
  .contact{position:absolute;left:13px;font-size:7px;line-height:1.35;color:var(--ink)}
  .contact h2{font-size:9px;font-weight:700;color:var(--navy)}
  .web{position:absolute;right:38px;top:367px;font-size:9px;font-weight:700;color:var(--navy)}
</style>
</head>
<body>

<section class="slide slide--title">
  <div class="network-bg" role="img" aria-label="Faint network of linked technology icons"></div>
  <p class="question">Does <strong>IT</strong> hear what troubles you?</p>
  <span class="brand">Pexlora</span>
  <div class="corner-fold"></div>
</section>

<section class="slide slide--cover">
  <div class="cover-photo" role="img" aria-label="Overhead photo of professionals walking across a bright office lobby"></div>
  <div class="cover-lockup"><span class="brand">Pexlora</span><span class="tag">Clear systems, calm teams</span></div>
  <div class="presenter-bar">
    <p class="name">Presenter's Name | Company Presentation</p>
    <p class="aud">To Business / Corporation</p>
  </div>
  <p class="cover-title">Presentation Title</p>
  <p class="cover-date">Feb 2014</p>
</section>

<section class="slide slide--portrait">
  <header class="header-dark"><h1>Image in Portrait view</h1><span class="sub">With an example of use of typography</span></header>
  <p class="drop-hint">Drag &amp; Drop images here <span class="arrow">→</span><br>It's an Image Placeholder</p>
  <p class="body-copy"><b>Lorem</b> ipsum dolor sit amet, consectetur adipiscing elit. Vivamus eget elit eu velit vehicula feugiat. Integer viverra metus vitae lectus dictum eleifend. Lorem ipsum dolor sit amet. Donec viverra lobortis feugiat. Sed id odio ante.</p>
  <ul class="tick-list"><li>Bibendum</li><li>Metus</li><li>Placerat</li></ul>
  <div class="image-slot">
    <svg width="82" height="82" viewBox="0 0 82 82" aria-hidden="true">
      <rect x="2" y="2" width="78" height="78" fill="none" stroke="#2f7cc0" stroke-width="4"/>
      <circle cx="24" cy="24" r="7" fill="#2f7cc0"/>
      <polygon points="10,70 30,40 42,55 56,32 74,70" fill="#2f7cc0"/>
    </svg>
  </div>
  <footer class="footer-light">
    <span class="brand">Pexlora</span>
    <span class="footer-meta">Company Presentation | <span>To <b>Business</b>/Corporation</span></span>
    <span class="page">3</span>
  </footer>
</section>

<section class="slide slide--graphs">
  <header class="header-light"><h1>Color Style Graphs</h1><span class="sub"><b>Main</b> and <b>Secondary</b> color themes</span></header>
  <p class="graph-title" style="left:25px;top:62px"><b>Graph</b> Main Colors</p>
  <p class="graph-title" style="left:293px;top:62px"><b>Graph</b> Secondary Colors</p>
  <svg class="charts" width="516" height="386" viewBox="0 0 516 386" style="position:absolute;left:0;top:0" aria-label="Area chart and pie chart">
    <g stroke="#dfe3e8" stroke-width=".6">
      <line x1="44" y1="100" x2="232" y2="100"/><line x1="44" y1="137.5" x2="232" y2="137.5"/>
      <line x1="44" y1="175" x2="232" y2="175"/><line x1="44" y1="212.5" x2="232" y2="212.5"/>
      <line x1="44" y1="250" x2="232" y2="250" stroke="#9aa1ab"/>
    </g>
    <g font-family="Lato,sans-serif" font-size="6.5" fill="var(--brand-blue)" text-anchor="end">
      <text x="38" y="102">100</text><text x="38" y="140">75</text><text x="38" y="177">50</text><text x="38" y="215">25</text><text x="38" y="252">0</text>
    </g>
    <g font-family="Lato,sans-serif" font-size="6.5" fill="var(--navy)" text-anchor="middle">
      <text x="48" y="259">2007</text><text x="108" y="259">2008</text><text x="170" y="259">2009</text><text x="230" y="259">2010</text>
    </g>
    <polygon points="44,167 107,186 162,155 232,176 232,250 44,250" fill="var(--navy)"/>
    <polygon points="44,219 80,222 107,214 44,250" fill="#8fd0ee"/>
    <polygon points="44,232 107,212 170,172 232,104 232,250 44,250" fill="var(--brand-blue)"/>
    <polygon points="44,219 74,226 44,232" fill="#8fd0ee"/>

    <path d="M372 175 L339.2 250.1 A82 82 0 0 1 400.0 97.9 Z" fill="var(--sky)"/>
    <path d="M372 175 L436.9 125.0 A82 82 0 0 1 451.95 193.2 Z" fill="var(--pink)"/>
    <path d="M372 175 L451.95 193.2 A82 82 0 0 1 339.2 250.1 Z" fill="var(--purple)"/>
    <path d="M376.7 168.5 L404.7 91.4 A82 82 0 0 1 441.6 118.5 Z" fill="var(--green)" stroke="#fff" stroke-width="1"/>
    <g font-family="Lato,sans-serif" font-size="8.5" fill="#fff" text-anchor="middle">
      <text x="336" y="147">50%</text><text x="421" y="115">9%</text><text x="427" y="155">14%</text><text x="356" y="223">28%</text>
    </g>
    <g font-family="Lato,sans-serif" font-size="6.5" fill="var(--navy)">
      <circle cx="462" cy="222" r="3" fill="var(--green)"/><text x="469" y="224.5">2007</text>
      <circle cx="462" cy="231.5" r="3" fill="var(--pink)"/><text x="469" y="234">2008</text>
      <circle cx="462" cy="241" r="3" fill="var(--purple)"/><text x="469" y="243.5">2009</text>
      <circle cx="462" cy="250.5" r="3" fill="var(--sky)"/><text x="469" y="253">2010</text>
    </g>
  </svg>
  <ul class="graph-notes" style="left:36px;top:270px">
    <li><b>Aenean</b> ridiculus tortor quis interdum id habitant ad, natoque consectetuer nisl auctor libero quisque euismod malesuada.</li>
    <li>Varius inceptos <b>nascetur</b> mollis dui aptent ultrices. Pretium pulvinar ante lobortis convallis lectus netus vitae eros.</li>
  </ul>
  <ul class="graph-notes" style="left:289px;top:270px">
    <li><b>Aenean</b> ridiculus tortor quis interdum id habitant ad, natoque consectetuer nisl auctor libero quisque euismod malesuada.</li>
    <li>Varius inceptos <b>nascetur</b> mollis dui aptent ultrices. Pretium pulvinar ante lobortis convallis lectus netus vitae eros.</li>
  </ul>
  <footer class="footer-dark">
    <span class="brand">Pexlora</span>
    <span class="footer-meta">Company Presentation | <span>To <b>Business</b>/Corporation</span></span>
  </footer>
  <div class="page-tab">4</div>
</section>

<section class="slide slide--tables">
  <header class="header-light"><h1>Color Style Tables</h1><span class="sub">Choose from a <b>light</b> or <b>dark</b> theme</span></header>
  <p class="table-title" style="left:22px">
    <svg width="14" height="11" viewBox="0 0 14 11" aria-hidden="true"><rect x=".5" y=".5" width="13" height="10" fill="none" stroke="var(--brand-blue)"/><path d="M.5 3.5h13M.5 7h13M5 .5v10M9.5 .5v10" stroke="var(--brand-blue)" stroke-width=".8"/></svg>
    Light Theme</p>
  <p class="table-title" style="left:270px">
    <svg width="14" height="11" viewBox="0 0 14 11" aria-hidden="true"><rect x=".5" y=".5" width="13" height="10" fill="none" stroke="var(--brand-blue)"/><path d="M.5 3.5h13M.5 7h13M5 .5v10M9.5 .5v10" stroke="var(--brand-blue)" stroke-width=".8"/></svg>
    Dark Theme</p>

  <table class="task-table task-table--light">
    <colgroup><col style="width:28px"><col style="width:89px"><col style="width:59px"><col style="width:54px"></colgroup>
    <thead><tr><th>Item</th><th>Step/Action</th><th>Responsible</th><th>Target Date</th></tr></thead>
    <tbody>
      <tr><td>1</td><td>Business X, Y, Z high level needs</td><td>Business X, Y, Z</td><td>5/24/2013</td></tr>
      <tr><td>2</td><td>Understand current situation and safety mana</td><td>Business X, Y, Z</td><td>5/31/2013</td></tr>
      <tr><td>3</td><td>Submit Proposal</td><td>Business X, Y, Z</td><td>6/3/2013</td></tr>
      <tr><td>4</td><td>Review Proposal</td><td>Business X, Y, Z</td><td>TBD</td></tr>
      <tr><td>5</td><td>Prepare Final Proposal &amp; Statement of Work (SOW)</td><td>Business X, Y, Z</td><td>TBD</td></tr>
      <tr><td>6</td><td>Complete and sign SOW</td><td>Business X, Y, Z</td><td>TBD</td></tr>
      <tr><td>7</td><td>Schedule project start date</td><td>Business X, Y, Z</td><td>TBD</td></tr>
      <tr><td>8</td><td>Kick-off Project</td><td>Business X, Y, Z</td><td>TBD</td></tr>
      <tr><td>9</td><td>Complete Project</td><td>Business X, Y, Z</td><td>TBD</td></tr>
    </tbody>
    <tfoot><tr><td colspan="4">* Additional Information</td></tr></tfoot>
  </table>

  <table class="task-table task-table--dark">
    <colgroup><col style="width:28px"><col style="width:89px"><col style="width:59px"><col style="width:54px"></colgroup>
    <thead><tr><th>Item</th><th>Step/Action</th><th>Responsible</th><th>Target Date</th></tr></thead>
    <tbody>
      <tr><td>1</td><td>Business X, Y, Z high level needs</td><td>Business X, Y, Z</td><td>5/24/2013</td></tr>
      <tr><td>2</td><td>Understand current situation and safety mana</td><td>Business X, Y, Z</td><td>5/31/2013</td></tr>
      <tr><td>3</td><td>Submit Proposal</td><td>Business X, Y, Z</td><td>6/3/2013</td></tr>
      <tr><td>4</td><td>Review Proposal</td><td>Business X, Y, Z</td><td>TBD</td></tr>
      <tr><td>5</td><td>Prepare Final Proposal &amp; Statement of Work (SOW)</td><td>Business X, Y, Z</td><td>TBD</td></tr>
      <tr><td>6</td><td>Complete and sign SOW</td><td>Business X, Y, Z</td><td>TBD</td></tr>
      <tr><td>7</td><td>Schedule project start date</td><td>Business X, Y, Z</td><td>TBD</td></tr>
      <tr><td>8</td><td>Kick-off Project</td><td>Business X, Y, Z</td><td>TBD</td></tr>
      <tr><td>9</td><td>Complete Project</td><td>Business X, Y, Z</td><td>TBD</td></tr>
    </tbody>
    <tfoot><tr><td colspan="4">* Additional Information</td></tr></tfoot>
  </table>

  <footer class="footer-dark">
    <span class="brand">Pexlora</span>
    <span class="footer-meta">Company Presentation | <span>To <b>Business</b>/Corporation</span></span>
  </footer>
  <div class="page-tab">5</div>
</section>

<section class="slide slide--closing">
  <div class="network-bg" role="img" aria-label="Faint network of linked technology icons"></div>
  <div class="closing-brand"><span class="brand">Pexlora</span></div>
  <p class="closing-tag">Clear systems, calm teams</p>
  <div class="contact" style="top:280px">
    <h2>Contact Us:</h2>
    <p>Phone: 301-555-0142</p>
    <p>Fax: 301-555-0187</p>
    <p>Emergency Support: 240-555-0163</p>
  </div>
  <div class="contact" style="top:328px">
    <h2>Central Office:</h2>
    <p>48 Meridian Way</p>
    <p>Suite 210</p>
    <p>Rockport, MD 20900</p>
  </div>
  <p class="web">www.pexlora.com</p>
  <div class="corner-fold"></div>
</section>

</body>
</html>
```